Business Card design for amazing new Dental Office

Please read this brief closely!

Our client is a modern new dental office/
They love their new logo.
Now it's time to create a business card for them.

It should be a two sided card:
Side one should have the logo and name and maybe a color background or design.
Side two should have all the contact information which is here:

Marcus Holloway, D.D.S
General and Cosmetic Dentistry
4187 W. Pinecrest Avenue
Ventura, CA 93011
(805) 912-4386
drmarcus@bluefernsmiles-example.com
www.bluefernsmiles-example.com

Feel free to arrange that info as you like and to style both sides of the card according to your creativity. This is a chance for you to show your design skills!

Client is open to font choices and is looking for a style that is amazing and premium. Colors can be selected from the logo, or any variation of those.

You will not win this contest with a less than beautiful card design so please feel free to make multiple submissions.

Logo files attached and please message me with any questions.
Thanks!

Target Market(s)

Families and Professionals seeking dental services

Industry/Entity Type

Dental

Contact Information for Business Card

Logo, style, contact info as per the brief

Font styles to use
Sans Serif

Requirements
Must have
• Client's logo and contact details as per brief
Nice to have
• Unique style reflecting high end dental clinic near the beach
Should not have
• Must not look like a template

```html
<!DOCTYPE html>
<html lang="en">
<head>
<meta charset="utf-8">
<title>Blue Fern Smiles — Business Card</title>
<link rel="stylesheet" href="https://fonts.googleapis.com/css2?family=Montserrat:wght@400;500&display=swap">
<style>
  :root {
    --page: #eef1f4;
    --card-white: #ffffff;
    --sky: #5ab2de;
    --teal: #6ccbd0;
    --sand: #e9a862;
    --sun: #d9c152;
    --name-blue: #3fb2e6;
    --ink: #3a3f45;
    --icon-blue: #7cc6ea;
    --lip: #e9a59c;
    --shadow: rgba(30, 60, 90, 0.18);
  }
  * { box-sizing: border-box; margin: 0; padding: 0; }
  html, body { width: 1200px; height: 800px; overflow: hidden; }
  body {
    background: var(--page);
    font-family: "Montserrat", sans-serif;
    display: flex;
    align-items: center;
    justify-content: center;
    gap: 50px;
  }
  .card {
    width: 525px;
    height: 300px;
    border-radius: 4px;
    position: relative;
    overflow: hidden;
    box-shadow: 0 14px 34px var(--shadow);
  }

  /* Front side */
  .card-front {
    background: linear-gradient(160deg, var(--sky) 0%, var(--teal) 38%, var(--sand) 66%, var(--sun) 100%);
    display: flex;
    flex-direction: column;
    align-items: center;
    justify-content: center;
    color: #fff;
  }
  .brand-mark {
    display: flex;
    align-items: center;
    gap: 14px;
  }
  .brand-dot {
    width: 26px;
    height: 26px;
    border-radius: 50%;
    background: #fff;
  }
  .brand-name {
    font-weight: 400;
    font-size: 38px;
    letter-spacing: 0.08em;
    text-transform: uppercase;
    line-height: 1;
  }
  .brand-sub {
    margin-top: 12px;
    font-weight: 400;
    font-size: 14px;
    letter-spacing: 0.9em;
    text-transform: uppercase;
    padding-left: 0.9em;
  }

  /* Back side */
  .card-back { background: var(--card-white); }
  .back-brand {
    position: absolute;
    left: 34px;
    top: 36px;
    display: flex;
    align-items: center;
    gap: 8px;
    color: var(--name-blue);
    font-weight: 500;
    font-size: 14px;
    letter-spacing: 0.04em;
  }
  .back-brand .brand-dot { width: 12px; height: 12px; background: var(--name-blue); }
  .smile-photo {
    position: absolute;
    left: 0;
    bottom: 0;
    width: 200px;
    height: 170px;
  }
  .contact-block {
    position: absolute;
    left: 208px;
    top: 40px;
    right: 20px;
  }
  .doctor-name {
    color: var(--name-blue);
    font-weight: 500;
    font-size: 19px;
    letter-spacing: 0.02em;
  }
  .doctor-title {
    color: var(--ink);
    font-size: 12.5px;
    margin-top: 3px;
    letter-spacing: 0.02em;
  }
  .contact-list {
    list-style: none;
    margin-top: 24px;
    display: flex;
    flex-direction: column;
    gap: 10px;
  }
  .contact-item {
    display: flex;
    align-items: flex-start;
    gap: 10px;
    color: var(--ink);
    font-size: 11.5px;
    line-height: 1.35;
  }
  .contact-icon { width: 15px; height: 15px; flex: none; margin-top: 1px; }
  .contact-icon * { fill: none; stroke: var(--icon-blue); stroke-width: 1.6; stroke-linecap: round; stroke-linejoin: round; }
</style>
</head>
<body>

  <section class="card card-front" aria-label="Card front">
    <div class="brand-mark">
      <span class="brand-dot"></span>
      <span class="brand-name">Blue Fern</span>
    </div>
    <div class="brand-sub">Smiles</div>
  </section>

  <section class="card card-back" aria-label="Card back">
    <div class="back-brand"><span class="brand-dot"></span>Blue Fern Smiles</div>

    <svg class="smile-photo" viewBox="0 0 200 170" role="img" aria-label="Close-up photograph of a bright smile">
      <defs>
        <linearGradient id="smileTone" x1="0" y1="1" x2="1" y2="0">
          <stop offset="0" stop-color="#f3d7cf"/>
          <stop offset="0.5" stop-color="var(--lip)"/>
          <stop offset="1" stop-color="#f7ece8"/>
        </linearGradient>
      </defs>
      <path d="M0 170 L0 110 C40 70 110 40 190 36 C150 60 120 100 80 170 Z" fill="url(#smileTone)"/>
    </svg>

    <div class="contact-block">
      <h1 class="doctor-name">Marcus Holloway, D.D.S</h1>
      <p class="doctor-title">General and Cosmetic Dentistry</p>
      <ul class="contact-list">
        <li class="contact-item">
          <svg class="contact-icon" viewBox="0 0 16 16"><path d="M4 2 L6 5 L5 6.5 C6 8.5 7.5 10 9.5 11 L11 10 L14 12 L12.5 14 C7 13.5 2.5 9 2 3.5 Z"/></svg>
          <span>(805) 912-4386</span>
        </li>
        <li class="contact-item">
          <svg class="contact-icon" viewBox="0 0 16 16"><rect x="2" y="4" width="12" height="9" rx="1"/><path d="M2 4.5 L8 9 L14 4.5"/></svg>
          <span>drmarcus@bluefernsmiles-example.com</span>
        </li>
        <li class="contact-item">
          <svg class="contact-icon" viewBox="0 0 16 16"><circle cx="8" cy="8" r="6"/><path d="M2 8 H14 M8 2 C5 5 5 11 8 14 M8 2 C11 5 11 11 8 14"/></svg>
          <span>www.bluefernsmiles-example.com</span>
        </li>
        <li class="contact-item">
          <svg class="contact-icon" viewBox="0 0 16 16"><path d="M8 15 C4 10 3 8 3 6 A5 5 0 0 1 13 6 C13 8 12 10 8 15 Z"/><circle cx="8" cy="6" r="1.8"/></svg>
          <span>4187 W. Pinecrest Avenue<br>Ventura, CA 93011</span>
        </li>
      </ul>
    </div>
  </section>

</body>
</html>
```